Asset tracing and investigation firm requires marketing brochure for services

We need a professional looking brochure with layout that supports the text that we have already drafted, is easy on the eye and can easily be navigated by clients either electronic/screen format or printed format. The wording is not finalised and all aspects need to be remain editable (including the logo and picture(s)) - preferably in Word or similarly accessible format.

```html
<!DOCTYPE html>
<html lang="en">
<head>
<meta charset="utf-8">
<title>Verant – Asset Tracing Services Brochure</title>
<link rel="stylesheet" href="https://fonts.googleapis.com/css2?family=Montserrat:wght@500;600;700;800&family=Arimo:wght@400;700&display=swap">
<style>
  :root {
    --navy: #1e2257;
    --brand-blue: #1f4f9c;
    --gold: #f0b323;
    --paper: #ffffff;
    --backdrop: #dcdce0;
    --ink: #222222;
    --photo-sky: #6f9fd0;
    --photo-stone: #9a9a96;
    --photo-night: #4a4e56;
    --photo-dusk: #2c3038;
  }
  * { box-sizing: border-box; margin: 0; padding: 0; }
  html, body { width: 1104px; height: 1200px; overflow: hidden; }
  body {
    background: var(--backdrop);
    font-family: "Arimo", Arial, sans-serif;
    color: var(--ink);
    position: relative;
  }
  .spread {
    position: absolute;
    left: 142px;
    width: 820px;
    height: 560px;
    display: flex;
    box-shadow: 0 2px 8px rgba(0,0,0,0.12);
  }
  .spread--outer { top: 26px; }
  .spread--inner { top: 614px; }
  .page {
    position: relative;
    width: 410px;
    height: 560px;
    background: var(--paper);
    overflow: hidden;
  }

  /* Wordmark */
  .wordmark {
    display: flex;
    align-items: center;
    gap: 8px;
    font-family: "Montserrat", sans-serif;
    font-weight: 600;
    color: var(--brand-blue);
    letter-spacing: 1px;
  }
  .wordmark__square {
    background: var(--gold);
    display: block;
  }

  /* Back cover */
  .back-cover .wordmark {
    position: absolute;
    left: 0; right: 0; top: 196px;
    justify-content: center;
    font-size: 40px;
  }
  .back-cover .wordmark__square { width: 22px; height: 22px; }
  .contact {
    position: absolute;
    left: 0; right: 0; top: 455px;
    text-align: center;
    font-family: "Montserrat", sans-serif;
    font-weight: 500;
    font-size: 11px;
    line-height: 15px;
    color: #111;
  }

  /* Front cover */
  .front-cover .wordmark {
    position: absolute;
    left: 0; right: 0; top: 18px;
    justify-content: center;
    font-size: 38px;
  }
  .front-cover .wordmark__square { width: 20px; height: 20px; }
  .front-cover__rule {
    position: absolute;
    left: 108px; right: 108px; top: 72px;
    height: 3px;
    background: var(--gold);
  }
  .cover-photo {
    position: absolute;
    left: 0; right: 0; top: 91px; height: 314px;
    background: linear-gradient(160deg, var(--photo-stone) 0%, var(--photo-sky) 40%, #2f5f9e 65%, #3c4a4a 100%);
  }
  .cover-band {
    position: absolute;
    left: 0; right: 0; top: 405px; bottom: 0;
    background: var(--navy);
    text-align: center;
    font-family: "Montserrat", sans-serif;
  }
  .cover-band__name {
    margin-top: 22px;
    font-size: 31px;
    font-weight: 800;
    color: var(--gold);
    letter-spacing: 1px;
  }
  .cover-band__title {
    margin-top: 10px;
    font-size: 23px;
    font-weight: 600;
    line-height: 27px;
    color: #fff;
  }

  /* Inner pages */
  .bar {
    position: absolute;
    left: 0; right: 0;
    background: var(--navy);
  }
  .inner-photo {
    position: absolute;
    left: 0; right: 0;
  }
  .inner-photo--skyline {
    top: 0; height: 282px;
    background: linear-gradient(180deg, #6c7078 0%, var(--photo-night) 45%, #3a3a34 75%, #26292d 100%);
  }
  .inner-photo--night {
    top: 392px; bottom: 0;
    background: linear-gradient(180deg, #4c4a52 0%, var(--photo-dusk) 55%, #15181d 100%);
  }
  .copy {
    position: absolute;
    font-size: 8.3px;
    line-height: 10.2px;
    text-align: justify;
    color: #1a1a1a;
  }
  .copy h2 {
    font-family: "Arimo", sans-serif;
    font-weight: 700;
    font-size: 8.3px;
    color: var(--navy);
    text-transform: uppercase;
    margin-bottom: 3px;
  }
  .copy p { margin-bottom: 10px; }
  .copy--left p { margin-bottom: 6px; }
  .copy ul { list-style: none; margin-bottom: 10px; }
  .copy li::before { content: "•  "; }
  .copy--left { left: 26px; right: 22px; top: 304px; }
  .copy--right { left: 22px; right: 22px; top: 17px; }
</style>
</head>
<body>

<section class="spread spread--outer">
  <div class="page back-cover">
    <div class="wordmark"><span class="wordmark__square"></span>Verant</div>
    <p class="contact">0203 555 0148<br>hello@verant.co.uk<br>www.verant.co.uk</p>
  </div>
  <div class="page front-cover">
    <div class="wordmark"><span class="wordmark__square"></span>Verant</div>
    <div class="front-cover__rule"></div>
    <div class="cover-photo" role="img" aria-label="Upward view of city office towers, a curved glass skyscraper between stone buildings under blue sky"></div>
    <div class="cover-band">
      <p class="cover-band__name">VERANT</p>
      <p class="cover-band__title">ASSET TRACING<br>SERVICES</p>
    </div>
  </div>
</section>

<section class="spread spread--inner">
  <div class="page inner-left">
    <div class="inner-photo inner-photo--skyline" role="img" aria-label="City skyline at dusk by the water with a tall tower in the foreground"></div>
    <div class="bar" style="top:287px;height:4px"></div>
    <div class="copy copy--left">
      <h2>Who we are:</h2>
      <p>Verant are the asset tracing and investigation specialists for legal and corporate clients seeking fixed fee investigations, pre-sue and asset trace reports with fast turnarounds.</p>
      <h2>What we do:</h2>
      <p>We trace assets and gather crucial intelligence to inform your litigation strategy, bridge knowledge gaps, reduce risk and maximise recoveries. Our asset tracing and investigations services leverage advanced open source &amp; human intelligence with specialist wealth profiling techniques and detailed forensic analysis. We recognise the intricacies of medium and larger sized claims and represent maximum investigative insight and case relevance whilst keeping scope and fees proportionate to the matter in hand.</p>
      <h2>Cases:</h2>
      <p>We regularly conduct asset tracing and investigations on matters spanning Commercial Claims &amp; Disputes, Civil Litigation, Financial Fraud, Enforcement of an Order, Claims against a Director (including those on behalf of a Liquidator), Personal Injury, Employee Fraud, Unrepaid Loans, Investigation in respect of Bankrupt's Assets (on behalf of a Trustee), Matrimonial and Enforcement of Personal Guarantees.</p>
    </div>
    <div class="bar" style="bottom:0;height:6px"></div>
  </div>
  <div class="page inner-right">
    <div class="bar" style="top:0;height:6px"></div>
    <div class="copy copy--right">
      <h2>'Tessera' Asset Trace Reports:</h2>
      <p>We have developed a suite of Asset Tracing products to suit various budgets or quantum / nature of claim. In addition to tracing specific assets, the reports seek to help clients to manage certain other risks inherent in litigation / enforcement and exploit cost effective opportunities to maximise the scope for recovery through insight and intelligence. We do that by, in varying case-specific degrees, assessing matters through the prism of Asset Tracing, Wealth Profiling, Modus Operandi and Contextual Analysis.</p>
      <p>We recognize that there is no "one size fits all" solution and we treat every case on its individual merits and requirements. Nevertheless, our intention for the information that follows is to provide a steer, at least, for costs as well as a very broad guideline for investigation in the absence of a more formal scoping exercise.</p>
      <p>With that in mind, our 'Tessera' Asset Tracing products meticulously piece together our findings from a myriad of sources to provide an overall picture of the subject, circumstances, and context. For relatively basic pre-sue case, for example, our remit may be to:</p>
      <ul>
        <li>Trace physical assets such as residential, investment or commercial property, holiday homes, cars and vehicles, inheritance, private limited company business interests and beneficial ownership searches</li>
        <li>Conduct wealth profiling analysis so their lifestyle, background, family, trading history, solvency history, employment, and social media analysis</li>
        <li>Perform solvency due diligence through judgment, bankruptcy, credit, and other proprietary database searches</li>
      </ul>
      <p>Beyond these basic investigations, and moving through the Tessera levels, we assist on more complex cases trace additional assets (beyond the "low hanging fruit") and provide intelligence to bridge knowledge gaps</p>
    </div>
    <div class="bar" style="top:382px;height:4px"></div>
    <div class="inner-photo inner-photo--night" role="img" aria-label="Dark city skyline of glass towers at night under a cloudy sky"></div>
  </div>
</section>

</body>
</html>
```